Pavilune Global is looking for web design

I have a website that I made myself and I wanted to have a more professional design. go to my website www.PavilunePX.com and you will see what it is all about. My website was created with Weebly. we like to focus on that we have an earth friendly product. we offer a natural alternative to asphalt or concrete .

Target Market(s)

Landscape Archtects, Home Improvement , designers, parks and recreation

Industry/Entity Type

It Professional

Coding

Coded - Design and coding required

Number of Pages Required

5+ page

Requirements
Must have
• Landing page,
• Products Page contact us page

```html
<!DOCTYPE html>
<html lang="en">
<head>
<meta charset="utf-8">
<title>Pavilune Global</title>
<link rel="stylesheet" href="https://fonts.googleapis.com/css2?family=Open+Sans:wght@400;600;700&family=Roboto:wght@400;700&display=swap">
<style>
:root{
  --dark:#2b2b2b;
  --darker:#1e1e1e;
  --bar:#2f2f2f;
  --green:#8dc63f;
  --green-text:#8dc63f;
  --white:#ffffff;
  --ink:#111111;
  --body:#444444;
  --card:#efedec;
  --panel-grey:#d6d6d6;
  --submit:#7a5f55;
  --partner:#c4c4c4;
  --foot-text:#cfcfcf;
}
*{box-sizing:border-box;margin:0;padding:0}
html,body{width:1200px;height:2365px;overflow:hidden}
body{font-family:"Open Sans",Arial,sans-serif;background:var(--white);color:var(--body);position:relative}
.btn{display:inline-block;background:var(--green);color:var(--white);font-weight:600;text-align:center}

/* header */
.site-header{position:absolute;top:0;left:0;width:1200px;height:134px;background:var(--dark)}
.topbar{position:absolute;top:0;left:60px;right:60px;height:40px;border-bottom:1px solid #3d3d3d;font-size:12px;color:var(--white);display:flex;align-items:center}
.topbar .hours{flex:1}
.topbar .contact{display:flex;align-items:center;gap:8px;margin-right:40px}
.topbar .contact span{margin-right:16px}
.topbar .contact svg{width:12px;height:12px}
.topbar .social{display:flex;gap:4px}
.topbar .social i{width:18px;height:18px;border:1px solid #777;border-radius:50%;display:block}
.brand{position:absolute;left:62px;top:58px;display:flex;align-items:center;gap:14px}
.brand-dot{width:44px;height:44px;border-radius:50%;background:var(--green)}
.brand-name{font-size:26px;font-weight:600;letter-spacing:2px;color:var(--green);line-height:1}
.main-nav{position:absolute;right:60px;top:68px;display:flex;gap:0;font-size:14px;font-weight:600;color:var(--white)}
.main-nav a{padding:9px 13px;margin-left:10px}
.main-nav a.active{background:var(--green)}

/* hero */
.hero{position:absolute;top:134px;left:0;width:1200px;height:536px;background:linear-gradient(180deg,#6e8e5a 0%,#7fa060 35%,#8c7a68 60%,#6f5a4c 100%)}
.hero-caption{position:absolute;left:325px;top:183px;width:518px;height:120px;background:rgba(15,15,15,.88);text-align:center;padding-top:20px}
.hero-caption h1{font-size:47px;font-weight:400;color:var(--white);letter-spacing:1px;line-height:1}
.hero-caption p{font-size:15px;font-weight:600;color:var(--green-text);margin-top:10px}
.hero .btn{position:absolute;left:492px;top:319px;width:143px;height:52px;line-height:52px;font-size:17px}
.dots{position:absolute;left:566px;top:495px;display:flex;gap:4px}
.dots i{width:11px;height:11px;border-radius:50%;background:var(--white);display:block}
.dots i:first-child{background:#111}

/* features */
.features-title{position:absolute;top:728px;left:0;width:1200px;text-align:center;font-size:38px;font-weight:400;color:var(--ink);letter-spacing:1px}
.features-title::after{content:"";display:block;width:60px;height:5px;background:var(--green);margin:18px auto 0}
.card{position:absolute;top:836px;width:318px;height:481px;background:var(--card);text-align:center}
.card .photo{height:252px;width:100%}
.card .badge{position:absolute;left:124px;top:216px;width:72px;height:72px;border-radius:50%;background:var(--green);border:4px solid var(--white);display:flex;align-items:center;justify-content:center}
.card h3{font-size:17px;font-weight:600;color:var(--ink);margin-top:54px}
.card p{font-size:12.5px;line-height:19px;color:var(--body);margin:8px auto 0;width:250px}
.card .btn{position:absolute;left:95px;top:411px;width:129px;height:42px;line-height:42px;font-size:12px;font-weight:700}

/* about + form */
.about{position:absolute;top:1391px;left:0;width:647px;height:451px;background:var(--dark);padding:75px 0 0 60px;color:var(--white)}
.about h2{font-size:38px;font-weight:400;letter-spacing:1px;line-height:1}
.about h2::after{content:"";display:block;width:60px;height:5px;background:var(--white);margin-top:18px}
.about .lead{font-size:13.5px;font-weight:600;color:var(--green-text);margin-top:50px;width:540px;line-height:21px}
.about .text{font-size:13.5px;color:#ddd;margin-top:14px;width:540px;line-height:21px}
.about .btn{position:absolute;left:60px;top:323px;width:153px;height:47px;line-height:47px;font-size:16px}
.ask{position:absolute;top:1391px;left:647px;width:553px;height:451px;background:linear-gradient(135deg,#dcdcdc,#cfcfcf 50%,#d9d9d9)}
.ask-title{position:absolute;left:116px;top:40px;width:281px;height:44px;background:var(--white);border-left:10px solid var(--darker);font-size:16px;font-weight:600;color:var(--ink);text-align:center;line-height:44px}
.ask label{position:absolute;left:116px;font-size:13.5px;font-weight:600;color:var(--ink)}
.ask .field{position:absolute;left:116px;width:281px;height:37px;background:var(--white)}
.ask .submit{position:absolute;left:118px;top:376px;width:110px;height:38px;background:var(--submit);color:var(--white);font-size:14px;font-weight:600;text-align:center;line-height:38px}

/* partners */
.partners{position:absolute;top:1842px;left:0;width:1200px;height:153px;display:flex;justify-content:center;align-items:center;gap:90px}
.partners i{display:block;width:140px;height:34px;background:var(--partner);border-radius:4px}

/* footer */
.site-footer{position:absolute;top:1995px;left:0;width:1200px;height:328px;background:var(--darker);color:var(--foot-text)}
.col{position:absolute;top:52px}
.col h4{font-family:"Roboto",Arial,sans-serif;font-size:14px;font-weight:700;color:var(--white);margin-bottom:22px}
.col ul{list-style:none;font-size:12px}
.col li{margin-bottom:16px}
.col li::before{content:"›";margin-right:12px;color:var(--white)}
.about-col p{font-size:13.5px;line-height:26px;width:240px}
.about-col .btn{margin-top:18px;width:115px;height:37px;line-height:37px;font-size:13px}
.foot-social{display:flex;gap:12px;margin-top:24px}
.foot-social i{width:19px;height:19px;background:var(--white);border-radius:3px;display:block}
.contact-col div{display:flex;gap:14px;font-size:12.5px;line-height:22px;margin-bottom:10px}
.contact-col svg{width:14px;height:14px;flex:none;margin-top:4px}
.copyright{position:absolute;top:2323px;left:0;width:1200px;height:42px;background:var(--bar);color:var(--white);font-size:13px;font-weight:600;text-align:center;line-height:42px}
</style>
</head>
<body>

<header class="site-header">
  <div class="topbar">
    <span class="hours">We are open: Mon - Sat 9.00 - 16.00</span>
    <div class="contact">
      <svg viewBox="0 0 12 12"><path d="M3 1l2 2-1 2c1 2 2 3 4 4l2-1 2 2-2 2C5 12 0 7 1 3z" fill="var(--green)"/></svg>
      <span>(080) 5550-0142</span>
      <svg viewBox="0 0 12 12"><rect x="0" y="2" width="12" height="8" fill="var(--green)"/><path d="M0 2l6 5 6-5" stroke="var(--dark)" fill="none"/></svg>
      <span>support@pavilunemail.com</span>
    </div>
    <div class="social"><i></i><i></i><i></i><i></i></div>
  </div>
  <div class="brand"><span class="brand-dot"></span><span class="brand-name">PAVILUNE GLOBAL</span></div>
  <nav class="main-nav">
    <a class="active">Home</a><a>Products</a><a>Ask The Experts</a><a>Distributors</a><a>Contact Us</a><a>Media</a>
  </nav>
</header>

<section class="hero" role="img" aria-label="Photo of a paved garden path lined with planted beds leading to a pavilion">
  <div class="hero-caption">
    <h1>PAVISTONE EXT</h1>
    <p>soil * decomposed granite * sand * aggregate</p>
  </div>
  <span class="btn">Learn More</span>
  <div class="dots"><i></i><i></i><i></i><i></i></div>
</section>

<h2 class="features-title">WHY CHOOSE PAVILUNE</h2>

<article class="card" style="left:60px">
  <div class="photo" role="img" aria-label="Photo of a curving granite path through a park" style="background:linear-gradient(180deg,#8aa7c4,#5f8a4a 45%,#c9ad80 80%)"></div>
  <span class="badge"><svg width="30" height="30" viewBox="0 0 30 30"><path d="M15 4L5 15h6v11h8V15h6z" fill="#fff"/></svg></span>
  <h3>Decomposed granite stabilizer</h3>
  <p>Consequuntur magni netsum es qui ratione sequi nesciunt. Neque porro quisquat, quia voluptas</p>
  <span class="btn">LEARN MORE</span>
</article>

<article class="card" style="left:438px">
  <div class="photo" role="img" aria-label="Photo of a worker spraying sealant on a garden path" style="background:linear-gradient(180deg,#6f8f3e,#5f8b34 55%,#b79a6b)"></div>
  <span class="badge"><svg width="30" height="30" viewBox="0 0 30 30"><path d="M15 4L5 15h6v11h8V15h6z" fill="#fff"/></svg></span>
  <h3>Decomposed granite weather seal</h3>
  <p>Consequuntur magni netsum es qui ratione sequi nesciunt. Neque porro quisquat, quia voluptas</p>
  <span class="btn">LEARN MORE</span>
</article>

<article class="card" style="left:822px">
  <div class="photo" role="img" aria-label="Photo of two scientists examining a sample in a laboratory" style="background:linear-gradient(180deg,#b8b2a6,#d8d4cc 60%,#e8e6e2)"></div>
  <span class="badge"><svg width="30" height="30" viewBox="0 0 30 30"><path d="M15 4L5 15h6v11h8V15h6z" fill="#fff"/></svg></span>
  <h3>Custom Formulations</h3>
  <p>Consequuntur magni netsum es qui ratione sequi nesciunt. Neque porro quisquat, quia voluptas</p>
  <span class="btn">LEARN MORE</span>
</article>

<section class="about">
  <h2>WE ARE PAVILUNE</h2>
  <p class="lead">Sed ut perspiciatis unde omnis iste natus error sit voluptatem accusantium doloremque laudantium, totam rem</p>
  <p class="text">There are many variations of passages of Lorem Ipsum available, but the majority have suffered alteration in some form, by injected humour, or randomised words which don't look even slightly believable.</p>
  <span class="btn">Learn More</span>
</section>

<section class="ask">
  <div class="ask-title">Ask From Experts</div>
  <label style="top:127px">Full Name</label>
  <div class="field" style="top:149px"></div>
  <label style="top:207px">Email</label>
  <div class="field" style="top:229px"></div>
  <label style="top:284px">Comment</label>
  <div class="field" style="top:299px;height:62px"></div>
  <div class="submit">Submit</div>
</section>

<section class="partners" aria-label="Partners">
  <i></i><i></i><i></i><i></i><i></i>
</section>

<footer class="site-footer">
  <div class="col about-col" style="left:60px">
    <h4>About Us</h4>
    <p>Cum sociis natoque penatibus et magnis dis parturient montes, nascetur ridiculus mus. Morbi leo risus, porta.</p>
    <span class="btn">learn More</span>
    <div class="foot-social"><i></i><i></i><i></i><i></i><i></i><i></i></div>
  </div>
  <div class="col" style="left:384px">
    <h4>Client Information</h4>
    <ul><li>Our Attorneys</li><li>Practise Areas</li><li>Our Services</li><li>Latest News</li><li>Our Blog</li><li>Contact Information</li></ul>
  </div>
  <div class="col" style="left:671px">
    <h4>Customer Services</h4>
    <ul><li>Support Forums</li><li>Community Area</li><li>FAQ</li><li>Customer Feedback</li><li>Community Agent</li><li>Terms &amp; Conditions</li></ul>
  </div>
  <div class="col contact-col" style="left:940px">
    <h4>Contact Info</h4>
    <div><svg viewBox="0 0 14 14"><path d="M7 0a5 5 0 0 0-5 5c0 4 5 9 5 9s5-5 5-9a5 5 0 0 0-5-5z" fill="#fff"/><circle cx="7" cy="5" r="2" fill="var(--darker)"/></svg><span>27 Marlow Lane, N9 2QT<br>London, United Kingdom</span></div>
    <div><svg viewBox="0 0 14 14"><path d="M3 1l2 2-1 3c1 2 2 3 4 4l3-1 2 2-2 2C6 13 1 8 1 3z" fill="#fff"/></svg><span>+1800-555-0190</span></div>
    <div><svg viewBox="0 0 14 14"><rect x="1" y="3" width="12" height="8" fill="none" stroke="#fff"/><path d="M1 3l6 5 6-5" stroke="#fff" fill="none"/></svg><span>support@pavilunemail.com</span></div>
    <div><svg viewBox="0 0 14 14"><circle cx="7" cy="7" r="6" fill="none" stroke="#fff" stroke-width="1.5"/><path d="M7 3v4h3" stroke="#fff" fill="none"/></svg><span>Mon - Sat 9.00 - 16.00</span></div>
  </div>
</footer>

<div class="copyright">© Copyright 2016 by Pavilune | All rights reserved</div>

</body>
</html>
```